Note/Card sent to show appreciation to partners who worked with us to improve local communities

I'd like a simple note/card designed for a wide audience. Originally, I called this a "Thanksgiving Card," but it's really just a card to be sent around Thanksgiving, not specifically celebrating the Thanksgiving holiday. We plan to send the card out just prior to Thanksgiving 2017 (Nov. 24, 2017). I work at a regulated electric utility, and we'd like to say thank you to the many stakeholders who we partner with throughout the year to support initiatives that help to improve our state and create opportunities for economic growth. I'm interested mostly in the design of the card, not the simple verbiage on the inside.
Customers, charitable foundations, nonprofits, advocacy groups, industry associations, friends

```html
<!DOCTYPE html>
<html lang="en">
<head>
<meta charset="utf-8">
<title>Thanks Card</title>
<link rel="stylesheet" href="https://fonts.googleapis.com/css2?family=Libre+Baskerville&display=swap">
<style>
  :root {
    --backdrop: #d6d6d6;
    --orange-light: #f7ad2e;
    --orange-mid: #f0901f;
    --orange-deep: #e2661a;
    --purple-light: #8a4cb8;
    --purple-deep: #4a1f6e;
    --cream: #fff1dc;
    --white: #ffffff;
  }
  * { box-sizing: border-box; margin: 0; padding: 0; }
  html, body {
    width: 1200px;
    height: 960px;
    overflow: hidden;
    background: var(--backdrop);
  }
  .stage {
    width: 1200px;
    height: 960px;
    display: flex;
    align-items: center;
    justify-content: center;
  }
  .card {
    position: relative;
    width: 640px;
    height: 860px;
    overflow: hidden;
    background: radial-gradient(circle at 18% 65%, var(--orange-light) 0%, var(--orange-mid) 45%, var(--orange-deep) 100%);
  }
  .swooshes {
    position: absolute;
    inset: 0;
    width: 100%;
    height: 100%;
  }
  .brand {
    position: absolute;
    left: 66px;
    top: 92px;
    display: flex;
    align-items: center;
    gap: 12px;
    color: var(--white);
    font-family: "Libre Baskerville", serif;
    font-size: 22px;
    line-height: 1.2;
  }
  .brand-dot {
    width: 30px;
    height: 30px;
    border-radius: 50%;
    background: var(--white);
    flex: none;
  }
  .thanks-panel {
    position: absolute;
    left: 74px;
    top: 250px;
    width: 530px;
    height: 400px;
    background: linear-gradient(100deg, var(--purple-light) 0%, #6c36a0 50%, var(--purple-deep) 100%);
    display: flex;
    align-items: flex-end;
    justify-content: center;
    padding-bottom: 70px;
  }
  .thanks-word {
    position: relative;
    z-index: 1;
    color: var(--white);
    font-family: "Libre Baskerville", serif;
    font-size: 146px;
    line-height: 1;
    letter-spacing: -2px;
  }
  .panel-sheen {
    position: absolute;
    inset: 0;
    width: 100%;
    height: 100%;
  }
</style>
</head>
<body>
<main class="stage">
  <article class="card">
    <svg class="swooshes" viewBox="0 0 640 860" aria-hidden="true">
      <defs>
        <linearGradient id="swoosh-fade" x1="0" y1="0" x2="1" y2="0">
          <stop offset="0" stop-color="#fff1dc" stop-opacity="0.85"/>
          <stop offset="1" stop-color="#fff1dc" stop-opacity="0"/>
        </linearGradient>
      </defs>
      <path d="M330 0 C470 180 520 520 470 860 L560 860 C600 520 540 200 400 0 Z" fill="url(#swoosh-fade)" opacity="0.7"/>
      <path d="M400 0 C540 200 600 520 560 860 L600 860 C640 520 600 200 470 0 Z" fill="url(#swoosh-fade)" opacity="0.5"/>
    </svg>

    <div class="brand">
      <span class="brand-dot"></span>
      <span class="brand-name">Brightline Energy</span>
    </div>

    <section class="thanks-panel">
      <svg class="panel-sheen" viewBox="0 0 530 400" preserveAspectRatio="none" aria-hidden="true">
        <path d="M256 0 C380 120 430 260 410 400 L530 400 L530 0 Z" fill="#ffffff" opacity="0.12"/>
        <path d="M256 0 C330 100 360 220 350 400 L410 400 C430 260 380 120 256 0 Z" fill="#ffffff" opacity="0.1"/>
      </svg>
      <h1 class="thanks-word">thanks</h1>
    </section>
  </article>
</main>
</body>
</html>
```